Verpackungen für drei Naturheilprodukte und ein Verkaufsdisplay
Zielgruppe
Wir sind ein Team von drei Personen die sich das Ziel gesetzt haben möglichst viele Personen mit den Wirkstoffen aus der Natur zu erreichen. Wir sind der Überzeugung, dass die Wirkstoffe der Natur vorbeugend schlimmeres verhindern kann und auch auf sanfte Art und Weise dem Körber die Natürliche Energie zurückgeben kann.
Die Produkte werden laufend erweitert somit wird auch auf eine zukünftige Zusammenarbeit Wert gelegt.
Momentan arbeiten wir an folgenden Produkten die verpackt werden müssen:
- Bachblüten/CBD Globuli:
Diese wirken beruhigend, angstlösend stresslindernd. Die Verpackung wird aus einem Faltkarton sein (40mm x 35mm x 80mm)
- Hautpflege Salbe
Diese ist auch auf CBD und Kamillenblüten Basis. Diese wirkt entzündungshemmend, beschleunigt und unterstützt den Heilungsprozess. Die Creme ist in einem 30ml Glass.
- CBD Blüten (legales Cannabis).
Dies wirkt besonders Schmerzlindernd, krampflösend und entzündungshemmend. Die momentan verkaufte Sorte der Hanfblüte ist CBD Lumaris ca. 16% CBD/0,6% Gehalt THC (diese Angaben sollten einfach zu wechseln sein). Die Verpackung wird aus einem Faltkarton sein (ca. 60mm x 50mm x 80mm, für andere Vorschläge offen).
- Weiter stelle ich mir ein Ausstellungsdisplay vor. So Kompakt wie möglich, damit es gut auf dem Verkaufstresen platzfindet, jedoch trotzdem ins Auge sticht.
Aufgabenstellung
Sie Designen hier unsere Produktelinie momentan bestehend aus drei Produkten. Diese sollten ein einheitliches erscheinen und ein edles und schlichtes auftreten haben. Nicht Hanflastig. Das Hauptaugenmerk sollte eher auf Wellness, Gesundheit und Natur gesetzt sein. Den Rest lasse ich mich auf die Kreativität der Designer überraschen

```html
<!DOCTYPE html>
<html lang="de">
<head>
<meta charset="utf-8">
<title>Silvaro – Bachblüten CBD Globuli Verpackung</title>
<link rel="stylesheet" href="https://fonts.googleapis.com/css2?family=PT+Serif:ital,wght@0,400;0,700;1,400&family=Open+Sans:wght@400&display=swap">
<style>
  :root{
    --green:#8dc21f;
    --purple:#5c2a86;
    --purple-deep:#4e1f78;
    --lavender:#f1edf6;
    --ink:#3a3a3a;
    --muted:#6b6b6b;
    --line:#9a9a9a;
    --paper:#ffffff;
  }
  *{box-sizing:border-box;margin:0;padding:0}
  html,body{width:1200px;height:3137px;overflow:hidden;background:var(--paper)}
  body{position:relative;font-family:"PT Serif",Georgia,serif;color:var(--ink)}

  /* ---------- presentation stage ---------- */
  .stage{position:absolute;left:0;top:0;width:1200px;height:818px;
    background:linear-gradient(#ffffff 0%,#fbfbfb 60%,#ececec 100%)}
  .flat-side{position:absolute;left:284px;top:170px;width:136px;height:512px;
    background:var(--lavender);border-top:9px solid var(--green);padding:22px 10px;
    font-size:8.6px;line-height:14px;color:var(--ink)}
  .flat-side p{margin-bottom:14px}
  .flat-front{position:absolute;left:420px;top:170px;width:143px;height:512px;
    background:var(--paper);border-top:9px solid var(--green);box-shadow:0 0 0 1px #e2e2e2;text-align:center}
  .flat-label{position:absolute;top:420px;width:162px;height:212px;border-top:6px solid var(--green);text-align:center}
  .flat-label.purple{left:519px;background:var(--purple);color:#fff}
  .flat-label.plain{left:731px;background:var(--paper);box-shadow:0 0 0 1px #e2e2e2}

  .size-caption{position:absolute;left:61px;top:862px;font-family:"Open Sans",Arial,sans-serif;
    font-size:13px;letter-spacing:2px;color:#666}

  /* ---------- brand lockup ---------- */
  .brand{display:flex;flex-direction:column;align-items:center}
  .brand-dot{width:40px;height:40px;border-radius:50%;background:var(--green);margin-bottom:6px}
  .brand-name{font-size:28px;line-height:30px;color:var(--purple)}
  .brand-tag{font-size:7px;color:var(--muted);display:flex;align-items:center;gap:4px;white-space:nowrap}
  .brand-tag::before,.brand-tag::after{content:"";width:14px;height:1px;background:var(--muted)}

  /* ---------- dieline ---------- */
  .dieline{position:absolute;left:300px;width:599px;height:650px}
  .dieline svg.cut{position:absolute;left:0;top:0}
  .cut path,.cut polygon,.cut line{fill:none;stroke:var(--line);stroke-width:1}
  .band{position:absolute;left:0;top:167px;width:599px;height:6px;background:var(--green)}
  .panel{position:absolute;top:173px;height:311px;font-size:8.6px;line-height:14px}
  .panel-a{left:0;width:160px;padding:22px 9px 10px;background:var(--paper)}
  .panel-b{left:160px;width:140px;padding:12px 9px}
  .panel-c{left:300px;width:160px;text-align:center;padding-top:22px;background:var(--paper)}
  .panel-d{left:460px;width:139px;padding:12px 9px}
  .panel p{margin-bottom:12px;text-align:justify}
  .panel ul{list-style:none;margin-bottom:12px}
  .panel li{position:relative;padding-left:9px;white-space:nowrap}
  .panel li::before{content:"";position:absolute;left:0;top:5px;width:4px;height:4px;border-radius:50%;background:var(--green)}
  .lead,.key{color:var(--purple)}
  .sign{font-style:italic;color:var(--purple)}
  .product{font-size:21px;line-height:26px;margin-top:58px;color:var(--ink);white-space:nowrap}
  .variant{font-size:16px;line-height:22px;color:var(--ink);white-space:nowrap}
  .claim{font-style:italic;color:var(--purple);font-size:10.5px;line-height:14px;margin-top:26px}
  .volume{font-size:9px;margin-top:18px}
  .panel-a .info{margin-top:34px}
  .address{position:absolute;left:9px;top:268px;width:142px;font-size:8px;line-height:10px}
  .seal{position:absolute;right:0;top:-4px;width:34px;height:34px;border-radius:50%;border:1px solid #aaa}
  .lot{position:absolute;left:0;top:522px;width:160px;padding:42px 0 0 22px;font-size:10.5px;line-height:19px;color:var(--ink)}
  .lot span{display:inline-block;width:52px}
  .tuck-url{position:absolute;left:300px;top:104px;width:160px;text-align:center;font-size:7.5px;color:var(--purple)}
  .small-brand .brand-dot{width:38px;height:38px}
  .small-brand .brand-name{font-size:26px}

  .v-purple .panel-b,.v-purple .panel-d{background:var(--purple-deep);color:#fff}
  .v-purple .lead,.v-purple .panel-b .sign,.v-purple .panel-d .sign{color:var(--green)}
  .v-purple .panel-a .lead{color:var(--purple)}
  .v-purple .panel-b .sign,.v-purple .panel-d .sign{position:absolute;bottom:10px;left:9px}
  .v-soft .panel-b,.v-soft .panel-d{background:var(--lavender)}
  .v-soft .panel li::before,.v-plain .panel li::before{background:var(--purple)}
  .v-soft .panel-b .sign,.v-soft .panel-d .sign{position:absolute;top:270px;left:9px}
  .v-plain .panel-b,.v-plain .panel-d{background:var(--paper)}
  .v-plain .mid-band{position:absolute;top:298px;height:156px;background:var(--lavender)}
  .v-plain .foot-strip{position:absolute;top:454px;left:0;width:599px;height:30px;background:var(--lavender)}
  .v-plain .foot-strip span{position:absolute;top:9px;font-size:8px;text-align:center}
</style>
</head>
<body>

<section class="stage">
  <div class="flat-side">
    <p style="color:var(--purple);font-weight:700">Natürlich Kuren mit der ganzen Pflanze für Ihr Wohlbefinden.</p>
    <p>Lorem ipsum dil dolor godfsit amet, dfgdgjh consete eduftur sadipscing elitr, sefdshd diam nonumy sghdd eirmod sgwkg tempor invidunt fjfut labore et dolore magna adliquyam erat, sed diam voluptua.</p>
    <p>Lorem ipsum dhskdokl dolor consete eduftur sadipscing: diam nonumy sghdd, eirmod tempor invidunt, fjfut labore et dolore magna, adliquyam erat, sed diam.</p>
    <p>Lorem ipsum dil dolor godfsit amet, dfgdgjh consete eduftur sadipscing elitr, sefdshd diam.</p>
    <p style="color:var(--purple);font-style:italic;font-weight:700">Natürlich Kuren mit Silvaro.</p>
  </div>
  <div class="flat-front">
    <div class="brand" style="margin-top:50px"><div class="brand-dot" style="width:58px;height:58px"></div><div class="brand-name" style="font-size:34px;line-height:40px">Silvaro</div><div class="brand-tag">Natürlich Kuren</div></div>
    <div style="font-size:24px;color:var(--green);margin-top:88px">Bachblüten</div>
    <div style="font-size:19px;margin-top:8px">CBD Globuli</div>
    <div style="font-style:italic;color:var(--purple);font-size:13px;line-height:18px;margin-top:60px">Beruhigend, angstlösend<br>&amp; stresslindernd</div>
    <div style="font-size:13px;margin-top:34px">50 ml ℮</div>
  </div>
  <div class="flat-label purple">
    <div class="brand" style="margin-top:20px"><div class="brand-dot" style="width:34px;height:34px"></div><div class="brand-name" style="color:#fff;font-size:22px;line-height:24px">Silvaro</div></div>
    <div style="color:var(--green);font-size:18px;margin-top:26px">Bachblüten</div>
    <div style="font-size:11px;margin-top:2px">CBD Globuli</div>
    <div style="font-size:8px;margin-top:42px">50 ml ℮</div>
  </div>
  <div class="flat-label plain">
    <div class="brand" style="margin-top:20px"><div class="brand-dot" style="width:34px;height:34px"></div><div class="brand-name" style="font-size:22px;line-height:24px">Silvaro</div></div>
    <div style="color:var(--green);font-size:18px;margin-top:26px">Bachblüten</div>
    <div style="font-size:11px;margin-top:2px">CBD Globuli</div>
    <div style="font-size:8px;margin-top:42px">50 ml ℮</div>
  </div>
</section>

<div class="size-caption">PACKAGING 40 MM x 35 MM x 80 MM</div>

<!-- dieline 1 : purple side panels -->
<div class="dieline v-purple" style="top:926px">
  <svg class="cut" width="599" height="650" viewBox="0 0 599 650">
    <path d="M300,167 V40 Q300,0 340,0 H420 Q460,0 460,40 V167"/>
    <line x1="300" y1="45" x2="460" y2="45"/>
    <polygon points="160,167 172,61 294,61 300,167"/>
    <polygon points="460,167 466,61 581,61 599,167"/>
    <polygon points="160,484 172,588 294,588 300,484"/>
    <polygon points="300,484 305,588 456,588 460,484"/>
    <polygon points="460,484 466,588 581,588 599,484"/>
    <path d="M0,173 V620 Q0,649 30,649 H130 Q160,649 160,620 V484"/>
    <line x1="0" y1="603" x2="160" y2="603"/>
    <path d="M0,173 V484 H599 V173"/>
  </svg>
  <div class="tuck-url">www.silvaro.example</div>
  <div class="band"></div>
  <div class="panel panel-a">
    <div class="brand small-brand"><div class="brand-dot"></div><div class="brand-name">Silvaro</div><div class="brand-tag">Natürlich Kuren</div></div>
    <p class="info"><span class="key">Inhaltsstoffe:</span> Lorem afdf ipsum dil dolor sit dgg jasda amet, consete eduftur sadipsc do ing elitr, sefdshd</p>
    <p><span class="key">Verzehrempfehlung:</span> Nehmen Sie 4x pro Tag 4 Tropfen. Einfach direkt aus der Flasche auf die Zunge. Möglichst lange im Mund belassen.</p>
    <div class="address">Silvaro GmbH<br>D-12345 Musterstadt<br>www.silvaro.example<div class="seal"></div></div>
  </div>
  <div class="panel panel-b">
    <p class="lead">Natürlich Kuren mit der ganzen Pflanze für Ihr Wohlbefinden.</p>
    <p>Lorem ipsum dil dolor godfsit amet, dfgdgjh consete eduftur sadipscing elitr, sefdshd diam nonumy sghdd eirmod sgwkg tempor invidunt fjfut labore et dolore magna adliquyam erat, sed diam voluptua.</p>
    <p style="margin-bottom:0">Lorem ipsum dhskdokl dolor consete eduftur sadipscing:</p>
    <ul><li>diam nonumy sghdd</li><li>eirmod tempor invidunt</li><li>fjfut labore et dolore magna</li><li>adliquyam erat, sed diam</li></ul>
    <div class="sign">Natürlich Kuren mit Silvaro.</div>
  </div>
  <div class="panel panel-c">
    <div class="brand small-brand"><div class="brand-dot"></div><div class="brand-name">Silvaro</div><div class="brand-tag">Natürlich Kuren</div></div>
    <div class="product">Bachblüten</div><div class="variant">CBD Globuli</div>
    <div class="claim">Beruhigend, angstlösend<br>&amp; stresslindernd</div>
    <div class="volume">50 ml ℮</div>
  </div>
  <div class="panel panel-d">
    <p class="lead">Natürlich Kuren mit der ganzen Pflanze für Ihr Wohlbefinden.</p>
    <p>Lorem ipsum dil dolor godfsit amet, dfgdgjh consete eduftur sadipscing elitr, sefdshd diam nonumy sghdd eirmod sgwkg tempor invidunt fjfut labore et dolore magna adliquyam erat, sed diam voluptua.</p>
    <p style="margin-bottom:0">Lorem ipsum dhskdokl dolor consete eduftur sadipscing:</p>
    <ul><li>diam nonumy sghdd</li><li>eirmod tempor invidunt</li><li>fjfut labore et dolore magna</li><li>adliquyam erat, sed diam</li></ul>
    <div class="sign">Natürlich Kuren mit Silvaro.</div>
  </div>
  <div class="lot"><span>LOT:</span>18AA072GH<br><span>⌛</span>03 / 2022</div>
</div>

<!-- dieline 2 : soft lavender side panels -->
<div class="dieline v-soft" style="top:1652px">
  <svg class="cut" width="599" height="650" viewBox="0 0 599 650">
    <path d="M300,167 V40 Q300,0 340,0 H420 Q460,0 460,40 V167"/>
    <line x1="300" y1="45" x2="460" y2="45"/>
    <polygon points="160,167 172,61 294,61 300,167"/>
    <polygon points="460,167 466,61 581,61 599,167"/>
    <polygon points="160,484 172,588 294,588 300,484"/>
    <polygon points="300,484 305,588 456,588 460,484"/>
    <polygon points="460,484 466,588 581,588 599,484"/>
    <path d="M0,173 V620 Q0,649 30,649 H130 Q160,649 160,620 V484"/>
    <line x1="0" y1="603" x2="160" y2="603"/>
    <path d="M0,173 V484 H599 V173"/>
  </svg>
  <div class="tuck-url" style="color:var(--muted)">www.silvaro.example</div>
  <div class="band"></div>
  <div class="panel panel-a">
    <div class="brand small-brand"><div class="brand-dot"></div><div class="brand-name">Silvaro</div><div class="brand-tag">Natürlich Kuren</div></div>
    <p class="info"><span class="key">Inhaltsstoffe:</span> Lorem ipsum dolor se dolor godfsit amet, dfgdgjh consete eduftur dassadipscing elitr, sefdshd diam nonumy sghdd eirmod sgwkg.</p>
    <p><span class="key">Verzehrempfehlung:</span> Nehmen Sie 4x pro Tag 4 Tropfen. Einfach direkt aus der Flasche auf die Zunge. Möglichst lange im Mund belassen.</p>
    <div class="address">Silvaro GmbH<br>D-12345 Musterstadt<br>www.silvaro.example<div class="seal"></div></div>
  </div>
  <div class="panel panel-b">
    <p class="lead">Natürlich Kuren mit der ganzen Pflanze für Ihr Wohlbefinden.</p>
    <p>Lorem ipsum dil dolor godfsit amet, dfgdgjh consete eduftur sadipscing elitr, sefdshd diam nonumy sghdd eirmod sgwkg tempor invidunt fjfut labore et dolore magna adliquyam erat, sed diam voluptua.</p>
    <p style="margin-bottom:0">Lorem ipsum dhskdokl dolor consete eduftur sadipscing:</p>
    <ul><li>diam nonumy sghdd</li><li>eirmod tempor invidunt</li><li>fjfut labore et dolore magna</li><li>adliquyam erat, sed diam</li></ul>
    <div class="sign">Natürlich Kuren mit Silvaro.</div>
  </div>
  <div class="panel panel-c">
    <div class="brand small-brand"><div class="brand-dot"></div><div class="brand-name">Silvaro</div><div class="brand-tag">Natürlich Kuren</div></div>
    <div class="product">Bachblüten</div><div class="variant">CBD Globuli</div>
    <div class="claim">Beruhigend, angstlösend<br>&amp; stresslindernd</div>
    <div class="volume">50 ml ℮</div>
  </div>
  <div class="panel panel-d">
    <p class="lead">Natürlich Kuren mit der ganzen Pflanze für Ihr Wohlbefinden.</p>
    <p>Lorem ipsum dil dolor godfsit amet, dfgdgjh consete eduftur sadipscing elitr, sefdshd diam nonumy sghdd eirmod sgwkg tempor invidunt fjfut labore et dolore magna adliquyam erat, sed diam voluptua.</p>
    <p style="margin-bottom:0">Lorem ipsum dhskdokl dolor consete eduftur sadipscing:</p>
    <ul><li>diam nonumy sghdd</li><li>eirmod tempor invidunt</li><li>fjfut labore et dolore magna</li><li>adliquyam erat, sed diam</li></ul>
    <div class="sign">Natürlich Kuren mit Silvaro.</div>
  </div>
  <div class="lot"><span>LOT:</span>18AA072GH<br><span>⌛</span>03 / 2022</div>
</div>

<!-- dieline 3 : plain with lavender band -->
<div class="dieline v-plain" style="top:2378px">
  <svg class="cut" width="599" height="650" viewBox="0 0 599 650">
    <path d="M300,167 V40 Q300,0 340,0 H420 Q460,0 460,40 V167"/>
    <line x1="300" y1="45" x2="460" y2="45"/>
    <polygon points="160,167 172,61 294,61 300,167"/>
    <polygon points="460,167 466,61 581,61 599,167"/>
    <polygon points="160,484 172,588 294,588 300,484"/>
    <polygon points="300,484 305,588 456,588 460,484"/>
    <polygon points="460,484 466,588 581,588 599,484"/>
    <path d="M0,173 V620 Q0,649 30,649 H130 Q160,649 160,620 V484"/>
    <line x1="0" y1="603" x2="160" y2="603"/>
  </svg>
  <div class="tuck-url" style="color:var(--muted)">www.silvaro.example</div>
  <div class="band"></div>
  <div class="panel panel-a" style="background:transparent">
    <div class="brand small-brand"><div class="brand-dot"></div><div class="brand-name">Silvaro</div><div class="brand-tag">Natürlich Kuren</div></div>
  </div>
  <div class="mid-band" style="left:0;width:160px"></div>
  <div class="mid-band" style="left:300px;width:160px"></div>
  <div class="panel panel-a" style="background:transparent;padding-top:146px">
    <p style="margin-bottom:0">Lorem ipsum dil dolor sit amet consete eduftur sadipscing elitr</p>
    <ul><li>sefdshd diam nonumy sghdd</li><li>eirmod sgwkg tempor invidunt</li><li>fjfut labore et dolore magna</li><li>adliquyam erat, sed diam</li></ul>
    <div class="address" style="top:240px">Silvaro GmbH<br>D-12345 Musterstadt<br>www.silvaro.example<div class="seal"></div></div>
  </div>
  <div class="panel panel-b">
    <p class="lead">Natürlich Kuren mit der ganzen Pflanze für Ihr Wohlbefinden.</p>
    <p><span class="key">Inhaltsstoffe:</span> Lorem ipsum dil dolor sit amet, consete eduftur sadipscing elitr, sefdshd diam nonumy sghdd eirmod sgwkg tempor invidunt fjfut labore et dolore magna adliquyam erat, sed diam voluptua.</p>
    <p><span class="key">Verzehrempfehlung:</span> Nehmen Sie 4x pro Tag 4 Tropfen. Einfach direkt aus der Flasche auf die Zunge. Möglichst lange im Mund belassen. Sie können die Tropfen auch in Getränke geben.</p>
  </div>
  <div class="panel panel-c" style="background:transparent">
    <div class="brand small-brand"><div class="brand-dot"></div><div class="brand-name">Silvaro</div><div class="brand-tag">Natürlich Kuren</div></div>
    <div class="product">Bachblüten</div><div class="variant">CBD Globuli</div>
    <div class="claim">Beruhigend, angstlösend<br>&amp; stresslindernd</div>
  </div>
  <div class="panel panel-d">
    <p class="lead">Natürlich Kuren mit der ganzen Pflanze für Ihr Wohlbefinden.</p>
    <p><span class="key">Inhaltsstoffe:</span> Lorem ipsum dil dolor sit amet, consete eduftur sadipscing elitr, sefdshd diam nonumy sghdd eirmod sgwkg tempor invidunt fjfut labore et dolore magna adliquyam erat, sed diam voluptua.</p>
    <p><span class="key">Verzehrempfehlung:</span> Nehmen Sie 4x pro Tag 4 Tropfen. Einfach direkt aus der Flasche auf die Zunge. Möglichst lange im Mund belassen. Sie können die Tropfen auch in Getränke geben.</p>
  </div>
  <div class="foot-strip">
    <span style="left:0;width:160px">50 ml ℮</span>
    <span style="left:160px;width:140px">www.silvaro.example</span>
    <span style="left:300px;width:160px">50 ml ℮</span>
    <span style="left:460px;width:139px">www.silvaro.example</span>
  </div>
  <svg class="cut" width="599" height="650" viewBox="0 0 599 650">
    <path d="M0,173 V484 H599 V173"/>
    <line x1="160" y1="173" x2="160" y2="484"/>
    <line x1="300" y1="173" x2="300" y2="484"/>
    <line x1="460" y1="173" x2="460" y2="484"/>
  </svg>
  <div class="lot"><span>LOT:</span>18AA072GH<br><span>⌛</span>03 / 2022</div>
</div>

</body>
</html>
```